Buchcover-Design für Fragenbuch
Ganz herzlichen Dank. Die Zusammenarbeit war völlig reibungslos und entspannt. Änderungswünsche wurden professionell umgesetzt und die kreativen Vorschläge fand ich super. Ich bin total glücklich mit dem Ergebnis.
Zielgruppe
Autorin und Workshopleiterin. Zielgruppe: Frauen ab 30
Aufgabenstellung
Ich benötige ein komplettes Buchcover, sowie 12 farbige Innenseiten. Es geht um ein Fragenbuch zum Ausfüllen mit dem Titel:
„Finde zurück zur leisen Mitte
Ein Arbeitsheft zum Eintragen für tiefere seelische Ruhe“
Das Format des Buches beträgt 17x22cm. Es ist in 12 Wochen unterteilt. Darum hätte ich gerne zwischen den einzelnen Wochen eine farbige Seite (1. Woche, 2. Woche etc.), die designmäßig mit dem Außencover korrespondiert.
Die Farben sollten eher zart oder gedeckt sein. Auf keinen Fall jedoch kitschig. Wichtig ist mir, dass keine bestimmte Person zu sehen ist. (Foto)
Das ist meine Website www.finde-zurueck-zur-leisen-mitte.de

```html
<!DOCTYPE html>
<html lang="de">
<head>
<meta charset="utf-8">
<title>Finde zurück zur leisen Mitte – Buchcover</title>
<link href="https://fonts.googleapis.com/css2?family=Amatic+SC:wght@400&family=Figtree:wght@300;400&display=swap" rel="stylesheet">
<style>
  :root {
    --paper: #f2f6ef;
    --ink-blue: #1d6888;
    --terracotta: #c4694b;
    --silhouette: #000000;
    --wash-teal: #2f8a9a;
    --wash-green: #74ab82;
    --wash-blue: #1f6d9c;
  }
  html, body {
    margin: 0;
    padding: 0;
    width: 927px;
    height: 1200px;
    overflow: hidden;
    background: var(--paper);
  }
  .cover {
    position: relative;
    width: 927px;
    height: 1200px;
    background: var(--paper);
    overflow: hidden;
  }
  .cover__author {
    position: absolute;
    left: 76px;
    top: 164px;
    margin: 0;
    font-family: "Figtree", sans-serif;
    font-weight: 300;
    font-size: 41px;
    letter-spacing: 1px;
    color: var(--ink-blue);
    line-height: 1;
  }
  .cover__title {
    position: absolute;
    left: 70px;
    top: 226px;
    margin: 0;
    font-family: "Figtree", sans-serif;
    font-weight: 300;
    font-size: 88px;
    line-height: 94px;
    letter-spacing: 0.5px;
    color: var(--terracotta);
  }
  .cover__subtitle {
    position: absolute;
    left: 77px;
    top: 430px;
    margin: 0;
    font-family: "Amatic SC", cursive;
    font-weight: 400;
    font-size: 46px;
    line-height: 1;
    letter-spacing: 0.5px;
    color: var(--ink-blue);
    white-space: nowrap;
  }
  .cover__artwork {
    position: absolute;
    left: 158px;
    top: 600px;
    width: 612px;
    height: 600px;
    border-radius: 300px 300px 0 0;
    background:
      radial-gradient(ellipse 52% 58% at 58% 62%, var(--wash-green) 0%, var(--wash-teal) 55%, var(--wash-blue) 78%, var(--silhouette) 80%);
  }
</style>
</head>
<body>
  <main class="cover">
    <p class="cover__author">Helene Marwitz</p>
    <h1 class="cover__title">Finde zurück zur<br>leisen Mitte</h1>
    <p class="cover__subtitle">Ein Arbeitsheft zum Eintragen für tiefere seelische Ruhe</p>
    <div class="cover__artwork" role="img" aria-label="Illustration: schwarze Silhouette eines Erwachsenenkopfes im Profil, darin die Silhouette eines Kinderkopfes in blau-grüner Aquarellfarbe"></div>
  </main>
</body>
</html>
```